Vesit cards for web development company

We need a business card design for our company. The company develops online platforms and conducts marketing consulting. Company logo. The cards must fit in with us (a junior start UP), but they must also be professional enough to impress with investors like banks. We wish you a combination of classic and modern design

Target Market(s)

Business partners and IT and marketing customers

Industry/Entity Type

It Company

Contact Information for Business Card

Folgende Information Lena Hartwig.
Name, Position, Telefon Nr., Mobile Nr., E-Mail adresse, Optional sind noch Webadresse und HRB Nummer

Colors

Designer to choose colors to be used in the design.

Requirements
Must have
• The cards have to fit into the logo later and have to be dynamic and serious at the same time

```html
<!DOCTYPE html>
<html lang="en">
<head>
<meta charset="utf-8">
<title>Arvelo Development – Business Cards</title>
<link rel="stylesheet" href="https://fonts.googleapis.com/css2?family=Open+Sans:wght@400;600;700;800&display=swap">
<style>
  :root {
    --backdrop: #0b0b0b;
    --paper: #efefec;
    --paper-edge: #e4e4e1;
    --ink: #2b2b2b;
    --ink-soft: #4a4a4a;
    --brand-blue: #2277bd;
    --brand-navy: #1f4576;
    --frame-grey: #8c8c8c;
    --frame-dark: #3c3c3e;
    --white: #ffffff;
  }
  * { box-sizing: border-box; margin: 0; padding: 0; }
  html, body {
    width: 1200px; height: 1000px; overflow: hidden;
    background: var(--backdrop);
    font-family: "Open Sans", Arial, sans-serif;
  }
  .stage {
    position: relative; width: 1200px; height: 1000px;
    display: flex; align-items: center; justify-content: center; gap: 60px;
  }
  .card {
    position: relative; width: 520px; height: 300px;
    border-radius: 3px; overflow: hidden;
    box-shadow: 0 14px 30px rgba(0,0,0,.6);
  }

  /* Front: contact side */
  .card-front { background: var(--paper); color: var(--ink); }
  .contact { position: absolute; left: 34px; top: 40px; }
  .person-name { font-size: 19px; font-weight: 700; color: var(--ink); }
  .person-name .surname { color: var(--brand-blue); }
  .person-role { font-size: 13px; color: var(--ink-soft); margin-top: 1px; }
  .contact-list { list-style: none; margin-top: 18px; font-size: 13px; color: var(--ink-soft); }
  .contact-list li { display: flex; align-items: center; gap: 8px; line-height: 19px; }
  .contact-list .spacer { width: 12px; }
  .contact-list li + .group-start { margin-top: 6px; }
  .contact-list svg { width: 12px; height: 12px; fill: var(--brand-blue); flex: none; }

  .wordmark {
    display: flex; align-items: center; gap: 8px;
    font-weight: 800; letter-spacing: .5px; text-transform: uppercase;
  }
  .wordmark .dot { border-radius: 50%; flex: none; }
  .card-front .wordmark { position: absolute; right: 30px; top: 96px; font-size: 22px; color: var(--brand-blue); }
  .card-front .wordmark .dot { width: 16px; height: 16px; background: var(--brand-blue); }

  .legal { position: absolute; right: 30px; bottom: 28px; text-align: right; font-size: 13px; color: var(--ink-soft); line-height: 19px; }

  /* Back: brand side */
  .card-back { background: var(--paper-edge); }
  .frame-band-left { position: absolute; left: 0; top: 0; width: 44px; height: 100%; background: var(--frame-dark); }
  .frame-band-top { position: absolute; left: 0; top: 0; width: 70%; height: 22px; background: var(--frame-grey); }
  .frame-band-right { position: absolute; right: 0; top: 22px; width: 60px; height: 80%; background: var(--brand-navy); }
  .brand-panel {
    position: absolute; left: 28px; top: 22px; right: 28px; bottom: 28px;
    background: linear-gradient(160deg, #2f7fc2, var(--brand-blue));
    display: flex; align-items: center; justify-content: center;
  }
  .card-back .wordmark { font-size: 30px; color: var(--white); }
  .card-back .wordmark .dot { width: 22px; height: 22px; background: var(--white); }
</style>
</head>
<body>
<main class="stage">

  <section class="card card-front" aria-label="Business card, contact side">
    <div class="contact">
      <p class="person-name">Lena <span class="surname">Hartwig</span></p>
      <p class="person-role">Manager</p>
      <ul class="contact-list">
        <li><svg viewBox="0 0 12 12" aria-hidden="true"><path d="M2.5 1h2l1 3-1.4 1a6 6 0 0 0 3 3L8 6.5l3 1v2A1.5 1.5 0 0 1 9.5 11 8.5 8.5 0 0 1 1 2.5 1.5 1.5 0 0 1 2.5 1z"/></svg>+61 2345 678</li>
        <li><svg viewBox="0 0 12 12" aria-hidden="true"><path d="M3.5 0h5A1 1 0 0 1 9.5 1v10a1 1 0 0 1-1 1h-5a1 1 0 0 1-1-1V1a1 1 0 0 1 1-1zm.5 1.5v7.5h4V1.5z"/></svg>+61 8765 432</li>
        <li class="group-start"><svg viewBox="0 0 12 12" aria-hidden="true"><path d="M0 2h12v1L6 7 0 3zm0 2.5 6 4 6-4V10H0z"/></svg>lena.hartwig@arvelo.dev</li>
        <li><svg viewBox="0 0 12 12" aria-hidden="true"><path d="M0 2h12v1L6 7 0 3zm0 2.5 6 4 6-4V10H0z"/></svg>office@arvelo.dev</li>
      </ul>
    </div>

    <div class="wordmark"><span class="dot"></span>Arvelo Development</div>

    <div class="legal">
      <p>HRB number - 67890</p>
      <p>www.arvelo.dev</p>
    </div>
  </section>

  <section class="card card-back" aria-label="Business card, brand side">
    <div class="frame-band-left"></div>
    <div class="frame-band-top"></div>
    <div class="frame-band-right"></div>
    <div class="brand-panel">
      <div class="wordmark"><span class="dot"></span>Arvelo Development</div>
    </div>
  </section>

</main>
</body>
</html>
```